Postcard design to acquire new clients for my Property Management Company

I'm looking for a postcard design that I can send to prospective clients detailing information about my company and services.
Postcard should be eye catching and contain information from www.brightkeyrentals-example.com. I've provided a few screen shots for the most important information and my logo.
Target Market(s)
Real Estate
Industry/Entity Type
Real Estate
Font styles to use
Sans Serif
Requirements
Must have
- Must be eye catching!! this will be a direct mail piece - I'd like for the card to be read and not tossed in the trash immediately.
Design que from the logo.
A place to write / print the receipts name and address.
our physical address - 2287 Marble Lane, Lubbock, TX 79555.
Should not have
- the contact information on the business card is not accurate - please use info from website.

```html
<!DOCTYPE html>
<html lang="en">
<head>
<meta charset="utf-8">
<title>Postcard | Option 2</title>
<link href="https://fonts.googleapis.com/css2?family=Montserrat:wght@400;500;600;700&family=Oswald:wght@600&family=Roboto+Condensed:wght@400&display=swap" rel="stylesheet">
<style>
:root{
  --green:#6db843;
  --green-dark:#4e8f2c;
  --navy:#0f4c81;
  --band:#2d5688;
  --ink:#2b2b2b;
  --muted:#8a8a8a;
  --board:#efefef;
  --panel:#f3f5f8;
  --label:#4a4a4a;
}
*{margin:0;padding:0;box-sizing:border-box}
html,body{width:686px;height:1200px;overflow:hidden}
body{background:var(--board);font-family:'Montserrat',sans-serif;color:var(--ink);position:relative}
.board-header{position:absolute;left:0;top:0;width:686px;height:64px;background:#fff}
.board-title{position:absolute;left:48px;top:24px;font-family:'Roboto Condensed',sans-serif;font-size:16px;color:var(--label)}
.side-label{position:absolute;left:48px;font-size:14px;font-weight:500;color:var(--label);line-height:1.2}
.sheet{position:absolute;left:136px;width:514px;height:348px;background:#fff;box-shadow:0 0 2px rgba(0,0,0,.08)}
.card{position:absolute;left:11px;top:11px;width:492px;height:325px;overflow:hidden;background:#fff}
.photo{position:absolute;left:0;top:0;width:492px}
.photo-house{height:149px;background:linear-gradient(180deg,#3aa9e0 0%,#8fc5e4 30%,#b9a98a 55%,#7b7468 72%,#4f8a3a 100%)}
.photo-street{height:125px;background:linear-gradient(180deg,#9cc6e6 0%,#dfe9f1 40%,#c98a5a 58%,#d9d2c4 70%,#5e9a3c 100%)}

/* front */
.tier-band{position:absolute;left:0;top:0}
.tier-name{position:absolute;color:#fff;font-weight:700}
.tier-full{left:36px;top:108px;font-size:13px}
.tier-pop{left:36px;top:126px;font-size:8.5px;font-weight:700;color:#fff;position:absolute;display:flex;align-items:center;gap:3px}
.tier-lease{left:219px;top:133px;font-size:9px}
.tier-premium{left:363px;top:133px;font-size:9px}
.plan{position:absolute;top:158px;width:164px;text-align:center}
.plan-rate{display:flex;align-items:baseline;justify-content:center;gap:5px;height:22px}
.plan-rate b{font-size:18px;color:var(--navy);font-weight:600}
.plan-rate span{font-size:7px;color:var(--muted)}
.plan ul{list-style:none;margin-top:9px}
.plan li{font-size:7px;line-height:13.9px}
.plan .note{color:#666}
.plan-divider{position:absolute;top:164px;height:130px;border-left:1px dashed #bbb}
.contact-bar{position:absolute;left:0;top:305px;width:492px;height:20px;background:var(--navy)}
.contact-bar span{position:absolute;top:5px;color:#fff;font-size:7.4px;white-space:nowrap}
.contact-email{left:16px}
.contact-web{left:176px}
.call-tab{position:absolute;left:345px;top:274px}
.call-text{position:absolute;left:370px;top:280px;color:#fff;text-align:center;width:115px}
.call-text .call{font-size:12px;font-weight:500;display:flex;align-items:center;justify-content:center;gap:4px}
.call-text .phone{font-size:13px;font-weight:600;margin-top:2px}

/* back */
.title-band{position:absolute;left:0;top:0}
.headline{position:absolute;left:7px;top:79px;font-family:'Oswald',sans-serif;font-weight:600;color:#fff;font-size:18.5px;line-height:21px;letter-spacing:.2px}
.features{position:absolute;left:0;top:125px;width:329px;height:200px}
.features-green{background:var(--green)}
.feature{position:absolute;width:164px;height:49px}
.feature-icon{position:absolute;left:5px;top:10px;width:26px;height:26px;border-radius:50%;background:var(--green);display:flex;align-items:center;justify-content:center}
.features-green .feature-icon{background:var(--green-dark)}
.feature h3{position:absolute;left:38px;top:12px;font-size:7px;font-weight:600;color:#222}
.features-green .feature h3{color:#fff}
.feature p{position:absolute;left:38px;top:21px;width:120px;font-size:4.6px;line-height:7px;color:#777}
.features-green .feature p{color:#fff}
.feat-vline{position:absolute;left:159px;top:10px;height:185px;border-left:1px dashed #ccc}
.features-green .feat-vline{border-color:rgba(255,255,255,.5)}
.feat-hline{position:absolute;left:7px;width:307px;border-top:1px dashed #ccc}
.features-green .feat-hline{border-color:rgba(255,255,255,.5)}
.mail-panel{position:absolute;left:328px;top:125px;width:164px;height:200px}
.mail-panel-grey{background:var(--panel)}
.stamp{position:absolute;left:122px;top:10px;width:36px;height:54px;border:1px dashed #7a9cc4}
.address-line{position:absolute;left:13px;width:145px;border-top:1px dashed #7a9cc4}
.brand{position:absolute;left:0;top:158px;width:164px;text-align:center;color:var(--navy);font-weight:600}
.brand-name{font-size:15px;letter-spacing:2.5px;line-height:16px}
.brand-sub{font-size:6.3px;letter-spacing:1.5px}
</style>
</head>
<body>
<header class="board-header"><div class="board-title">Postcard | Option 2</div></header>

<div class="side-label" style="top:256px">FRONT</div>
<div class="side-label" style="top:593px">BACK<br>White Ver</div>
<div class="side-label" style="top:967px">BACK<br>Green Ver</div>

<!-- front -->
<section class="sheet" style="top:90px">
  <div class="card">
    <div class="photo photo-house" role="img" aria-label="Photo of a large brick family home with a double garage and trees"></div>
    <svg class="tier-band" width="492" height="149" viewBox="0 0 492 149">
      <path d="M0 93 H138 L158 125 H492 V149 H0 Z" fill="var(--green)"/>
    </svg>
    <div class="tier-name tier-full">FULL SERVICE</div>
    <div class="tier-pop"><svg width="11" height="11" viewBox="0 0 24 24"><path d="M12 2l3 7h7l-5.6 4.3 2.2 7.2L12 16l-6.6 4.5 2.2-7.2L2 9h7z" fill="#fff"/></svg>Our Most Popular</div>
    <div class="tier-name tier-lease">LEASE ONLY</div>
    <div class="tier-name tier-premium">PREMIUM SERVICE</div>

    <div class="plan" style="left:0">
      <div class="plan-rate"><b>10%</b><span>Monthly Rent</span></div>
      <ul>
        <li>Includes Leasing Service</li>
        <li>24/7 Emergency Response</li>
        <li>Move In &amp; Out Inspections</li>
        <li>Professional Lease Enforcement</li>
        <li>Schedule &amp; Oversee all Repairs</li>
        <li>Pay all Invoices</li>
        <li>Monthly &amp; Year End Statements</li>
        <li>Annual Market Rent Analysis</li>
      </ul>
    </div>
    <div class="plan-divider" style="left:164px"></div>
    <div class="plan" style="left:164px">
      <div class="plan-rate"><b>9%</b><span>Annual Lease</span></div>
      <ul style="margin-top:7px">
        <li>Professional Photography</li>
        <li>Marketing &amp; Advertising</li>
        <li>Property Showings</li>
        <li>Tenant Screening &amp;</li>
        <li>Qualifications</li>
        <li>Lease Execution</li>
        <li>Move In Coordination</li>
        <li class="note">* You just need tenants</li>
      </ul>
    </div>
    <div class="plan-divider" style="left:327px"></div>
    <div class="plan" style="left:327px">
      <div class="plan-rate"><b>12%</b><span>Monthly Rent</span></div>
      <ul style="margin-top:7px">
        <li>Includes Full Service Features</li>
        <li>Professional Video Marketing</li>
        <li>Home Warranty Coordination</li>
        <li>Tenant Retention Program</li>
      </ul>
    </div>

    <div class="contact-bar">
      <span class="contact-email">info@brightkeyrentals-example.com</span>
      <span class="contact-web">www.brightkeyrentals-example.com</span>
    </div>
    <svg class="call-tab" width="147" height="51" viewBox="0 0 147 51">
      <path d="M0 31 C18 31 22 22 32 10 C38 3 42 0 52 0 H147 V51 H0 Z" fill="var(--navy)"/>
    </svg>
    <div class="call-text">
      <div class="call"><svg width="14" height="14" viewBox="0 0 24 24" fill="none" stroke="#fff" stroke-width="1.6"><path d="M5 3h4l2 5-2.5 1.5a11 11 0 0 0 6 6L16 13l5 2v4a2 2 0 0 1-2 2A16 16 0 0 1 3 5a2 2 0 0 1 2-2z"/><path d="M15 3a6 6 0 0 1 6 6M15 7a2 2 0 0 1 2 2"/></svg>CALL US</div>
      <div class="phone">(806)-555-0147</div>
    </div>
  </div>
</section>

<!-- back, white -->
<section class="sheet" style="top:450px">
  <div class="card">
    <div class="photo photo-street" role="img" aria-label="Photo of a suburban street with tiled-roof houses and green trees"></div>
    <svg class="title-band" width="492" height="125" viewBox="0 0 492 125">
      <path d="M0 70 H290 C300 70 306 74 312 80 L322 90 C328 96 334 98 344 98 H492 V125 H0 Z" fill="var(--band)" opacity=".95"/>
    </svg>
    <h2 class="headline">WE OFFER FULL-SERVICE PROPERTY<br>MANAGEMENT SOLUTIONS</h2>

    <div class="features">
      <div class="feat-vline"></div>
      <div class="feat-hline" style="top:51px"></div>
      <div class="feat-hline" style="top:100px"></div>
      <div class="feat-hline" style="top:148px"></div>
      <div class="feature" style="left:0;top:0"><div class="feature-icon"><svg width="12" height="12" viewBox="0 0 24 24" fill="#fff"><path d="M12 3l10 9h-3v9h-5v-6h-4v6H5v-9H2z"/></svg></div><h3>PROPERTY MARKETING</h3><p>Tired of waiting for weeks on end, hoping to find a new tenant? Let us take over your marketing for you and we'll find a qualified renter quickly.</p></div>
      <div class="feature" style="left:163px;top:0"><div class="feature-icon"><svg width="14" height="12" viewBox="0 0 28 24" fill="#fff"><circle cx="9" cy="7" r="4"/><circle cx="19" cy="7" r="4"/><path d="M1 21c0-5 4-8 8-8s8 3 8 8zM15 21c0-3 1-5 3-7 5 0 9 3 9 7z"/></svg></div><h3>TENANT SCREENING</h3><p>We don't just find someone to rent your home — we find the best renters. We screen all applications using fair housing guidelines to protect you.</p></div>
      <div class="feature" style="left:0;top:49px"><div class="feature-icon"><span style="color:#fff;font-weight:700;font-size:14px">$</span></div><h3>RENT COLLECTION</h3><p>Stop guessing when you'll receive your rental earnings every month and say hello to consistent payments. We keep your tenants current.</p></div>
      <div class="feature" style="left:163px;top:49px"><div class="feature-icon"><svg width="12" height="12" viewBox="0 0 24 24" fill="#fff"><path d="M13 3l8 8-4 1-2-2-9 10-3-3 10-9-2-2z"/></svg></div><h3>MAINTENANCE</h3><p>Still scrambling to respond to repair requests every time you receive a tenant call? Let us coordinate repair work on your behalf!</p></div>
      <div class="feature" style="left:0;top:98px"><div class="feature-icon"><svg width="11" height="11" viewBox="0 0 24 24" fill="none" stroke="#fff" stroke-width="3.5"><circle cx="10" cy="10" r="6"/><path d="M15 15l6 6"/></svg></div><h3>PROPERTY INSPECTIONS</h3><p>Inspections form an important part of our proactive property management approach. We visit every home in our portfolio regularly.</p></div>
      <div class="feature" style="left:163px;top:98px"><div class="feature-icon"><svg width="12" height="12" viewBox="0 0 24 24" fill="#fff"><path d="M3 3h2v16h16v2H3z"/><rect x="7" y="11" width="3" height="6"/><rect x="12" y="7" width="3" height="10"/><rect x="17" y="9" width="3" height="8"/></svg></div><h3>FINANCIAL REPORTING</h3><p>Keep a handle on your real estate performance. We generate monthly statements so you can review income &amp; expenses at a moment's notice.</p></div>
      <div class="feature" style="left:0;top:146px"><div class="feature-icon"><svg width="11" height="12" viewBox="0 0 22 24" fill="#fff"><path d="M11 1l9 4v6c0 6-4 10-9 12C6 21 2 17 2 11V5z"/></svg></div><h3>EVICTIONS</h3><p>When things go wrong inside your rental home, rest easy with the experts on your side. We will handle evictions for you &amp; find new renters when its over.</p></div>
      <div class="feature" style="left:163px;top:146px"><div class="feature-icon"><svg width="14" height="12" viewBox="0 0 28 24" fill="none" stroke="#fff" stroke-width="2"><path d="M14 2v20M6 22h16M4 6h20M4 6l-3 8h6zM24 6l-3 8h6z"/></svg></div><h3>LEGAL GUIDANCE</h3><p>Don't accidentally violate one of the many ordinances and housing laws governing your relationship with your tenants. Let us keep you compliant.</p></div>
    </div>

    <div class="mail-panel mail-panel-grey">
      <div class="stamp"></div>
      <div class="address-line" style="top:92px"></div>
      <div class="address-line" style="top:111px"></div>
      <div class="brand"><div class="brand-name">BRIGHTKEY</div><div class="brand-sub">PROPERTY MANAGEMENT</div></div>
    </div>
  </div>
</section>

<!-- back, green -->
<section class="sheet" style="top:810px">
  <div class="card">
    <div class="photo photo-street" role="img" aria-label="Photo of a suburban street with tiled-roof houses and green trees"></div>
    <svg class="title-band" width="492" height="125" viewBox="0 0 492 125">
      <path d="M0 70 H290 C300 70 306 74 312 80 L322 90 C328 96 334 98 344 98 H492 V125 H0 Z" fill="var(--band)" opacity=".95"/>
    </svg>
    <h2 class="headline">WE OFFER FULL-SERVICE PROPERTY<br>MANAGEMENT SOLUTIONS</h2>

    <div class="features features-green">
      <div class="feat-vline"></div>
      <div class="feat-hline" style="top:51px"></div>
      <div class="feat-hline" style="top:100px"></div>
      <div class="feat-hline" style="top:148px"></div>
      <div class="feature" style="left:0;top:0"><div class="feature-icon"><svg width="12" height="12" viewBox="0 0 24 24" fill="#fff"><path d="M12 3l10 9h-3v9h-5v-6h-4v6H5v-9H2z"/></svg></div><h3>PROPERTY MARKETING</h3><p>Tired of waiting for weeks on end, hoping to find a new tenant? Let us take over your marketing for you and we'll find a qualified renter quickly.</p></div>
      <div class="feature" style="left:163px;top:0"><div class="feature-icon"><svg width="14" height="12" viewBox="0 0 28 24" fill="#fff"><circle cx="9" cy="7" r="4"/><circle cx="19" cy="7" r="4"/><path d="M1 21c0-5 4-8 8-8s8 3 8 8zM15 21c0-3 1-5 3-7 5 0 9 3 9 7z"/></svg></div><h3>TENANT SCREENING</h3><p>We don't just find someone to rent your home — we find the best renters. We screen all applications using fair housing guidelines to protect you.</p></div>
      <div class="feature" style="left:0;top:49px"><div class="feature-icon"><span style="color:#fff;font-weight:700;font-size:14px">$</span></div><h3>RENT COLLECTION</h3><p>Stop guessing when you'll receive your rental earnings every month and say hello to consistent payments. We keep your tenants current.</p></div>
      <div class="feature" style="left:163px;top:49px"><div class="feature-icon"><svg width="12" height="12" viewBox="0 0 24 24" fill="#fff"><path d="M13 3l8 8-4 1-2-2-9 10-3-3 10-9-2-2z"/></svg></div><h3>MAINTENANCE</h3><p>Still scrambling to respond to repair requests every time you receive a tenant call? Let us coordinate repair work on your behalf!</p></div>
      <div class="feature" style="left:0;top:98px"><div class="feature-icon"><svg width="11" height="11" viewBox="0 0 24 24" fill="none" stroke="#fff" stroke-width="3.5"><circle cx="10" cy="10" r="6"/><path d="M15 15l6 6"/></svg></div><h3>PROPERTY INSPECTIONS</h3><p>Inspections form an important part of our proactive property management approach. We visit every home in our portfolio regularly.</p></div>
      <div class="feature" style="left:163px;top:98px"><div class="feature-icon"><svg width="12" height="12" viewBox="0 0 24 24" fill="#fff"><path d="M3 3h2v16h16v2H3z"/><rect x="7" y="11" width="3" height="6"/><rect x="12" y="7" width="3" height="10"/><rect x="17" y="9" width="3" height="8"/></svg></div><h3>FINANCIAL REPORTING</h3><p>Keep a handle on your real estate performance. We generate monthly statements so you can review income &amp; expenses at a moment's notice.</p></div>
      <div class="feature" style="left:0;top:146px"><div class="feature-icon"><svg width="11" height="12" viewBox="0 0 22 24" fill="#fff"><path d="M11 1l9 4v6c0 6-4 10-9 12C6 21 2 17 2 11V5z"/></svg></div><h3>EVICTIONS</h3><p>When things go wrong inside your rental home, rest easy with the experts on your side. We will handle evictions for you &amp; find new renters when its over.</p></div>
      <div class="feature" style="left:163px;top:146px"><div class="feature-icon"><svg width="14" height="12" viewBox="0 0 28 24" fill="none" stroke="#fff" stroke-width="2"><path d="M14 2v20M6 22h16M4 6h20M4 6l-3 8h6zM24 6l-3 8h6z"/></svg></div><h3>LEGAL GUIDANCE</h3><p>Don't accidentally violate one of the many ordinances and housing laws governing your relationship with your tenants. Let us keep you compliant.</p></div>
    </div>

    <div class="mail-panel">
      <div class="stamp"></div>
      <div class="address-line" style="top:92px"></div>
      <div class="address-line" style="top:111px"></div>
      <div class="brand"><div class="brand-name">BRIGHTKEY</div><div class="brand-sub">PROPERTY MANAGEMENT</div></div>
    </div>
  </div>
</section>
</body>
</html>
```